rl ironcraft business card metallic look

revamp the existing design but want card to have a metalic look to it

Target Market(s)

construction industry

Industry/Entity Type

constrction

Contact Information for Business Card

front of card RL Ironcraft, phone 4163920857, email rl.ironcraftt@quellmail.example and instagram account; rl_ironcraft_

Font styles to use
Other font styles liked:
• masculine

Colors

Designer to choose only greyscale colors for use in the design.

Requirements
Must have
• back side RL Ironcraft then a list of everything : Siding, ACM Panels, Standing Seam,Soffit, Fascia, Gutters,Metal,Alu,inum, Viynyl, Metal Roofs and roof repairs
Nice to have
• I would like to keep the look of the existing card with the metal grids on the front
Should not have
• Need a design in two days

```html
<!DOCTYPE html>
<html lang="en">
<head>
<meta charset="utf-8">
<title>RL Ironcraft — Business Card</title>
<link href="https://fonts.googleapis.com/css2?family=Poppins:wght@500;700&display=swap" rel="stylesheet">
<style>
  :root {
    --stage: #2b2b2b;
    --card-dark: #141414;
    --card-mid: #1e1e1e;
    --card-edge: #0a0a0a;
    --rivet-light: #3a3a3a;
    --rivet-dark: #0b0b0b;
    --ink: #f2f2f2;
    --ink-soft: #bdbdbd;
    --name-steel: #8f8f8f;
    --name-deep: #050505;
  }
  * { margin: 0; padding: 0; box-sizing: border-box; }
  html, body { width: 1200px; height: 800px; overflow: hidden; }
  body {
    background: var(--stage);
    font-family: "Poppins", sans-serif;
    position: relative;
  }
  .card-pair {
    position: absolute;
    left: 40px;
    top: 245px;
    display: flex;
    gap: 40px;
  }
  .card {
    position: relative;
    width: 540px;
    height: 309px;
    border-radius: 3px;
    background:
      radial-gradient(ellipse at 30% 20%, rgba(255,255,255,0.05), transparent 60%),
      linear-gradient(135deg, var(--card-mid), var(--card-dark) 55%, var(--card-mid));
    box-shadow: 0 14px 30px rgba(0,0,0,0.55), inset 0 0 0 1px var(--card-edge);
    overflow: hidden;
  }
  .rivets { position: absolute; inset: 0; width: 100%; height: 100%; }

  /* front */
  .front-headline {
    position: absolute;
    left: 0; right: 0; top: 26px;
    text-align: center;
    font-weight: 700;
    font-size: 64px;
    letter-spacing: 2px;
    line-height: 1;
    color: var(--name-deep);
    text-transform: uppercase;
  }
  .front-name {
    position: absolute;
    left: 44px; bottom: 50px;
    font-weight: 700;
    font-size: 34px;
    line-height: 1.05;
    color: var(--name-steel);
    width: 210px;
  }
  .contact-list {
    position: absolute;
    left: 280px; top: 132px;
    list-style: none;
    display: flex;
    flex-direction: column;
    gap: 12px;
  }
  .contact-item {
    display: flex;
    align-items: center;
    gap: 10px;
    color: var(--ink);
    font-weight: 500;
    font-size: 14px;
  }
  .contact-icon { width: 16px; height: 16px; flex: none; }

  /* back */
  .back-name {
    position: absolute;
    left: 0; right: 0; top: 78px;
    text-align: center;
    font-weight: 700;
    font-size: 44px;
    color: var(--name-steel);
  }
  .service-list {
    position: absolute;
    left: 30px; right: 30px; top: 170px;
    text-align: center;
    color: var(--ink);
    font-weight: 500;
    font-size: 14px;
    line-height: 1.7;
  }
</style>
</head>
<body>
  <main class="card-pair">
    <section class="card card-front" aria-label="Front of card">
      <svg class="rivets" viewBox="0 0 540 309" aria-hidden="true">
        <defs>
          <radialGradient id="rivet-front" cx="0.35" cy="0.35" r="0.7">
            <stop offset="0" stop-color="#3a3a3a"/>
            <stop offset="1" stop-color="#0b0b0b"/>
          </radialGradient>
        </defs>
        <g fill="url(#rivet-front)">
          <circle cx="20" cy="20" r="7"/><circle cx="520" cy="20" r="7"/>
          <circle cx="20" cy="289" r="7"/><circle cx="520" cy="289" r="7"/>
          <circle cx="20" cy="154" r="7"/><circle cx="520" cy="154" r="7"/>
        </g>
      </svg>
      <div class="front-headline">RL Ironcraft</div>
      <div class="front-name">RL Ironcraft</div>
      <ul class="contact-list">
        <li class="contact-item">
          <svg class="contact-icon" viewBox="0 0 24 24" aria-hidden="true"><path fill="#bdbdbd" d="M6.6 10.8a15.1 15.1 0 0 0 6.6 6.6l2.2-2.2a1 1 0 0 1 1-.25 11.4 11.4 0 0 0 3.6.57 1 1 0 0 1 1 1V20a1 1 0 0 1-1 1A17 17 0 0 1 3 4a1 1 0 0 1 1-1h3.5a1 1 0 0 1 1 1c0 1.25.2 2.46.57 3.6a1 1 0 0 1-.25 1z"/></svg>
          <span>416-392-0857</span>
        </li>
        <li class="contact-item">
          <svg class="contact-icon" viewBox="0 0 24 24" aria-hidden="true"><path fill="#bdbdbd" d="M3 11 21 3l-8 18-2-8z"/></svg>
          <span>rl.ironcraftt@quellmail.example</span>
        </li>
        <li class="contact-item">
          <svg class="contact-icon" viewBox="0 0 24 24" aria-hidden="true"><circle cx="12" cy="12" r="8" fill="#bdbdbd"/></svg>
          <span>rl_ironcraft_</span>
        </li>
      </ul>
    </section>

    <section class="card card-back" aria-label="Back of card">
      <svg class="rivets" viewBox="0 0 540 309" aria-hidden="true">
        <defs>
          <radialGradient id="rivet-back" cx="0.35" cy="0.35" r="0.7">
            <stop offset="0" stop-color="#3a3a3a"/>
            <stop offset="1" stop-color="#0b0b0b"/>
          </radialGradient>
        </defs>
        <g fill="url(#rivet-back)">
          <circle cx="20" cy="20" r="7"/><circle cx="520" cy="20" r="7"/>
          <circle cx="20" cy="289" r="7"/><circle cx="520" cy="289" r="7"/>
          <circle cx="20" cy="154" r="7"/><circle cx="520" cy="154" r="7"/>
        </g>
      </svg>
      <div class="back-name">RL Ironcraft</div>
      <p class="service-list">
        Siding • ACM Panels • Standing Seam • Soffit • Fascia<br>
        Gutters • Metal • Alu • inum • Viynyl • Metal Roofs<br>
        and roof repairs
      </p>
    </section>
  </main>
</body>
</html>
```